Billboard Design for Modern Dispensary

Hello!
We need a eye-catching 12' x 24' billboard designed for a very successful, modern cannabis dispensary on the Oregon coast, United States. Because of rules, we cannot have any marijuana leafs or other cannabis related images (flower, joints, smoke, etc). We can use the words "Shop" or "Dispensary" - we cannot use the words "cannabis", "marijuana".

Some ideas we had are 3 words stacked on left or center of billboard - maybe across bottom we have horizontal logo and the following words - “South of bridge in Tidewell Bay”
Another idea is to have a small bubble in bottom/top corner with image of our dog (face only) - with some words around it - like "BONUS Shop Dog" or "Cute Shop Dog" or "Best Shop Dog" or "Friendly Staff"

here's some 3 word examples:
ENJOY
YOUR
TRIP

or

FEEL
GOOD
JUST
AHEAD

or

GOOD
VIBES
ONLY

or

GOOD
TIMES
CHILL
VIBES

I have attached our logo. I have also included a stacked logo version (vertical, not horizontal). the formats are .EPS and .PDF - the logos were created in Affinity Design 2.x.

Our website is coralnook.net if you want to see more images, etc about our dispensary.

Artwork Requirements:
The billboard is 12' tall x 25' wide
The artwork needs to be 1”=1’ @ 300dpi
Please add 6” of bleed all around so your total artwork is 13”x26”
Final deliverable should be .Ai file.

Font styles to use
Sans Serif

Colors
0054AA
0677BA
7BADD7
CADEEF
E8F1F8

Requirements
Nice to have
• See the project description - we included some ideas to consider.
Should not have
• No cannabis images, like flower, cannabis leaves, paraphenlia, cartridges, joints, etc.

```html
<!DOCTYPE html>
<html lang="en">
<head>
<meta charset="utf-8">
<title>Coral Nook — Sleep Better Tonight Billboard</title>
<link rel="stylesheet" href="https://fonts.googleapis.com/css2?family=League+Spartan:wght@800&family=Montserrat:wght@700;800&display=swap">
<style>
  :root {
    --ink: #000000;
    --brand-blue: #368CCB;
    --accent-blue: #4A9BD6;
    --pale-blue: #E8F1F8;
    --paper: #FBFCFE;
    --fur-light: #E3B877;
    --fur-deep: #B9813F;
    --portrait-bg: #F2ECDD;
  }
  * { margin: 0; padding: 0; box-sizing: border-box; }
  html, body { width: 1200px; height: 600px; overflow: hidden; }
  body { background: var(--paper); }
  .billboard {
    position: relative;
    width: 1200px;
    height: 600px;
    overflow: hidden;
    background: var(--paper);
  }
  .backdrop-pattern {
    position: absolute;
    inset: 0;
    background: linear-gradient(135deg, var(--paper) 0%, var(--pale-blue) 50%, var(--paper) 100%);
    opacity: 0.6;
  }
  .headline {
    position: absolute;
    left: 100px;
    top: 72px;
    font-family: "League Spartan", "Montserrat", sans-serif;
    font-weight: 800;
    font-size: 152px;
    line-height: 148px;
    letter-spacing: -1px;
    color: var(--ink);
    text-transform: uppercase;
  }
  .headline span { display: block; }
  .headline .highlight { color: var(--brand-blue); }
  .shop-dog-badge {
    position: absolute;
    left: 824px;
    top: 45px;
    width: 302px;
    height: 302px;
  }
  .brand-lockup {
    position: absolute;
    left: 766px;
    top: 411px;
    display: flex;
    align-items: center;
    gap: 14px;
  }
  .brand-mark {
    width: 90px;
    height: 90px;
    border-radius: 50%;
    border: 6px solid var(--accent-blue);
  }
  .brand-name {
    font-family: "Montserrat", sans-serif;
    font-weight: 800;
    font-size: 40px;
    color: var(--accent-blue);
    letter-spacing: 0.5px;
  }
  .location-line {
    position: absolute;
    left: 718px;
    top: 513px;
    font-family: "Montserrat", sans-serif;
    font-weight: 800;
    font-size: 25px;
    color: var(--accent-blue);
    white-space: nowrap;
  }
</style>
</head>
<body>
<main class="billboard">
  <div class="backdrop-pattern" role="img" aria-label="Faint pale blue leaf pattern across the background"></div>

  <h1 class="headline">
    <span>Sleep</span>
    <span class="highlight">Better</span>
    <span>Tonight</span>
  </h1>

  <svg class="shop-dog-badge" viewBox="0 0 302 302" aria-labelledby="badge-label">
    <title id="badge-label">Cute shop dog badge</title>
    <defs>
      <radialGradient id="dog-tones" cx="50%" cy="55%" r="55%">
        <stop offset="0%" stop-color="var(--fur-light)"/>
        <stop offset="65%" stop-color="var(--fur-deep)"/>
        <stop offset="100%" stop-color="var(--portrait-bg)"/>
      </radialGradient>
      <path id="badge-arc" d="M 46 151 A 105 105 0 0 1 256 151"/>
    </defs>
    <circle cx="151" cy="151" r="146" fill="var(--portrait-bg)" stroke="var(--brand-blue)" stroke-width="7"/>
    <circle cx="151" cy="165" r="110" fill="url(#dog-tones)" role="img" aria-label="Photo of the shop's golden doodle dog, face only"/>
    <text font-family="Montserrat, sans-serif" font-weight="800" font-size="23" fill="var(--brand-blue)" letter-spacing="1.5">
      <textPath href="#badge-arc" startOffset="50%" text-anchor="middle">CUTE SHOP DOG</textPath>
    </text>
  </svg>

  <div class="brand-lockup">
    <div class="brand-mark"></div>
    <span class="brand-name">CORAL NOOK</span>
  </div>

  <p class="location-line">South of bridge in Tidewell Bay</p>
</main>
</body>
</html>
```